Tri fold brochure for construction company

Looking for a tri fold brochure which utilizes black, teal and white colors. Logo must be on main page (several files with Logo attached)
Inside brochure.
1st Page - 3D photo/sketch/drawing of a complete residential high rise building with windows, balconies and elements of concrete and bricks.
2nd Page - Text which will outline company's main activities. file with text is attached.
3rd Page - photo/sketch/drawing of underground parking garage which shows columns/beams/walls/ and garage entrance/exit ramp. Can be multiple photos.
Back of brochure
1st page - company logo
2nd page - please propose something.
3rd page - company message with address and contact info (to be provided)
Back ground color of brochure should complement our logo/photos/sketches/drawings.
Alternative design options are welcome.

```html
<!DOCTYPE html>
<html lang="en">
<head>
<meta charset="UTF-8">
<title>Veridia Restoration Corp. – Tri-fold Brochure</title>
<link href="https://fonts.googleapis.com/css2?family=Montserrat:wght@400;500;600;700&display=swap" rel="stylesheet">
<style>
  :root {
    --teal: #18a58c;
    --teal-light: #6cc7b4;
    --charcoal: #4a4a4c;
    --charcoal-dark: #3d3d3f;
    --rule: #c9c9c9;
    --white: #ffffff;
    --ink: #555557;
  }
  * { box-sizing: border-box; margin: 0; padding: 0; }
  html, body { width: 1200px; height: 1200px; overflow: hidden; background: var(--white); }
  body { position: relative; font-family: 'Montserrat', sans-serif; }

  .brochure {
    position: absolute; left: 272px; top: 90px;
    width: 822px; height: 1276px;
    transform: scale(0.8); transform-origin: top left;
  }
  .sheet {
    position: absolute; left: 0; width: 822px; height: 636px;
    overflow: hidden; background: var(--white);
    box-shadow: 0 6px 30px rgba(0,0,0,0.25);
  }
  .sheet--outside { top: 0; }
  .sheet--inside { top: 640px; }
  .sheet__art { position: absolute; inset: 0; width: 822px; height: 636px; }

  .block { position: absolute; color: var(--white); }
  .title { font-weight: 700; font-size: 21px; line-height: 22px; text-transform: uppercase; }
  .title-rule { width: 122px; height: 3px; background: var(--rule); margin: 7px 0 12px; }
  .body-copy p { font-size: 11.2px; line-height: 14.6px; margin-bottom: 6px; }
  .justify p { text-align: justify; }

  .brand { text-align: center; color: var(--white); font-weight: 700; text-transform: uppercase; letter-spacing: 0.5px; display: flex; align-items: center; justify-content: center; gap: 8px; }
  .brand__mark { width: 12px; height: 12px; background: var(--teal); display: inline-block; }

  .contact { font-size: 11.5px; line-height: 15px; }
  .contact li { list-style: none; display: flex; gap: 6px; margin-bottom: 3px; }
  .contact svg { flex: none; margin-top: 2px; }
  .contact strong { font-weight: 700; }
  .accent { color: var(--teal); font-weight: 700; }

  .cover-title { text-align: center; font-weight: 700; font-size: 24px; line-height: 24px; text-transform: uppercase; }
  .cover-sub { text-align: center; font-weight: 700; font-size: 12px; margin-top: 10px; }
  .cover-rule { width: 180px; height: 3px; background: var(--rule); margin: 14px auto 10px; }
  .cover-web { text-align: center; font-size: 12px; display: flex; justify-content: center; gap: 5px; align-items: center; }

  .envelope-title { position: absolute; left: 290px; top: 28px; color: var(--teal); font-weight: 700; font-size: 21px; }
  .envelope-rule { position: absolute; left: 290px; top: 56px; width: 200px; height: 3px; background: var(--rule); }
  .service-col { position: absolute; color: var(--ink); }
  .service { margin-bottom: 9px; }
  .service h3 { color: var(--teal); font-size: 12.2px; font-weight: 700; text-transform: uppercase; display: flex; gap: 7px; }
  .service h3::before { content: "•"; }
  .service ul { list-style: none; padding-left: 19px; margin-top: 2px; }
  .service li { font-size: 9.6px; line-height: 11px; position: relative; margin-bottom: 2.5px; padding-left: 12px; }
  .service li::before { content: "·"; position: absolute; left: 0; }
</style>
</head>
<body>
<div class="brochure">

  <section class="sheet sheet--outside">
    <svg class="sheet__art" viewBox="0 0 822 636">
      <defs>
        <linearGradient id="gSite" x1="0" y1="0" x2="1" y2="1">
          <stop offset="0" stop-color="#c9d6e0"/><stop offset="1" stop-color="#8a7a66"/>
        </linearGradient>
        <linearGradient id="gHouse" x1="0" y1="0" x2="0" y2="1">
          <stop offset="0" stop-color="#bcd3e6"/><stop offset="0.55" stop-color="#e9e8e4"/><stop offset="1" stop-color="#7c6b58"/>
        </linearGradient>
      </defs>
      <g role="img" aria-label="Photo: two engineers in hard hats and safety vests reviewing plans on a site">
        <rect x="0" y="380" width="276" height="256" fill="url(#gSite)"/>
      </g>
      <path d="M0 0 H276 V420 C220 470 120 475 0 432 Z" fill="var(--teal)"/>
      <path d="M0 432 C120 475 220 470 276 420" fill="none" stroke="#bdbdbd" stroke-width="4"/>

      <g role="img" aria-label="Photo: modern multi-storey residential building with balconies, glass, stone and wood cladding">
        <rect x="276" y="0" width="546" height="480" fill="url(#gHouse)"/>
      </g>
      <polygon points="276,0 552,0 552,170" fill="var(--teal)"/>
      <polygon points="470,150 552,100 552,170" fill="var(--teal-light)"/>

      <path d="M552 0 H822 V160 C740 200 640 200 552 172 Z" fill="var(--charcoal)"/>
      <path d="M276 410 C340 370 450 365 552 398 L552 636 L276 636 Z" fill="var(--charcoal)"/>
      <path d="M470 470 L552 440 L552 636 L470 636 Z" fill="var(--charcoal-dark)" opacity="0.5"/>
      <path d="M552 430 C640 468 740 478 822 418 V636 H552 Z" fill="#9a9a9a"/>
      <path d="M552 446 C640 484 740 494 822 434 V636 H552 Z" fill="var(--teal)"/>
    </svg>

    <div class="block body-copy" style="left:24px; top:30px; width:230px;">
      <h2 class="title">About<br>Veridia</h2>
      <div class="title-rule"></div>
      <p>Alit moloratem ate derupta ssimus provit ut offic teces ius, sundigenis vid quis pres enimaximpel ipsuntore nihilles sequi sum velit autem. Nequi doluptatusam atem voloreprerio temostioreni unto consed ma aut a nonsequaepro ex ea vent aut quiatibus re modignihit, oditibus aspel il eium fugiat quaes nistotatur auditatius.</p>
      <p>Vit re necto quibusant dolut ipientiores millitas deniendam non re quidictur aut repere nobit, cori quaectur, quam ut volestem re lati deribus alique is saectet aut quae ommodit ommodi iliquant haris modit aliquo eum quae rempori bearibus asitat es dolectus.</p>
      <p>Metur, aut harum repro consedit aborum rent volorro venihic te voluptas molupturepd ex et et odit qui qui omnihil iquuntium que cus niaspedut optatem</p>
    </div>

    <div class="brand" style="position:absolute; left:276px; top:468px; width:276px; font-size:17px;">
      <span class="brand__mark"></span>Veridia
    </div>
    <ul class="block contact" style="left:310px; top:506px; width:240px;">
      <li><svg width="11" height="11" viewBox="0 0 12 12"><circle cx="6" cy="6" r="5.3" fill="none" stroke="var(--teal)"/><circle cx="6" cy="5" r="1.6" fill="var(--teal)"/></svg>
        <span><strong>Veridia Restoration Corp.</strong><br>418 Harbor Line Road, Eastvale<br>NW 30418</span></li>
      <li><svg width="11" height="11" viewBox="0 0 12 12"><circle cx="6" cy="6" r="5.3" fill="none" stroke="var(--teal)"/><path d="M4 3.5 L5 3 L6 5 L5 5.6 Q5.5 7 6.8 7.4 L7.4 6.4 L9 7.4 L8.5 8.6 Q5 8.6 3.6 4.6 Z" fill="var(--teal)"/></svg>
        <span class="accent">555-014-2270</span></li>
      <li><svg width="11" height="11" viewBox="0 0 12 12"><circle cx="6" cy="6" r="5.3" fill="none" stroke="var(--teal)"/><circle cx="6" cy="6" r="2.6" fill="none" stroke="var(--teal)"/></svg>
        <span>www.<span class="accent">veridiarestore</span>.com</span></li>
      <li><svg width="11" height="11" viewBox="0 0 12 12"><circle cx="6" cy="6" r="5.3" fill="none" stroke="var(--teal)"/><rect x="3.3" y="4" width="5.4" height="4" fill="none" stroke="var(--teal)"/></svg>
        <span>info@<strong>veridiarestore</strong>.com</span></li>
    </ul>

    <div class="brand" style="position:absolute; left:552px; top:124px; width:270px; font-size:23px;">
      <span class="brand__mark" style="width:14px;height:14px;"></span>Veridia
    </div>

    <div class="block" style="left:552px; top:488px; width:270px;">
      <h1 class="cover-title">About<br>Veridia</h1>
      <p class="cover-sub">Your subhead will go here!</p>
      <div class="cover-rule"></div>
      <p class="cover-web"><svg width="11" height="11" viewBox="0 0 12 12"><circle cx="6" cy="6" r="5.3" fill="none" stroke="#fff"/><circle cx="6" cy="6" r="2.6" fill="none" stroke="#fff"/></svg>
        <span>www.<strong>veridiarestore</strong>.com</span></p>
    </div>
  </section>

  <section class="sheet sheet--inside">
    <svg class="sheet__art" viewBox="0 0 822 636">
      <defs>
        <linearGradient id="gDrill" x1="0" y1="0" x2="1" y2="1"><stop offset="0" stop-color="#d6d6d2"/><stop offset="1" stop-color="#8f5a3e"/></linearGradient>
        <linearGradient id="gDesk" x1="0" y1="0" x2="1" y2="1"><stop offset="0" stop-color="#b08a5c"/><stop offset="1" stop-color="#e8e4dc"/></linearGradient>
        <linearGradient id="gTrowel" x1="0" y1="0" x2="1" y2="1"><stop offset="0" stop-color="#9b9690"/><stop offset="1" stop-color="#6d6862"/></linearGradient>
        <linearGradient id="gTablet" x1="0" y1="0" x2="1" y2="1"><stop offset="0" stop-color="#c7b9a2"/><stop offset="1" stop-color="#4a5660"/></linearGradient>
      </defs>
      <g role="img" aria-label="Photo: concrete core drilling machine on a worksite">
        <rect x="0" y="440" width="276" height="196" fill="url(#gDrill)"/>
      </g>
      <path d="M0 0 H276 V455 C210 505 110 505 0 470 Z" fill="var(--teal)"/>
      <path d="M0 470 C110 505 210 505 276 455" fill="none" stroke="#9a9a9a" stroke-width="5"/>

      <g role="img" aria-label="Photo: construction worker in a hard hat drafting plans at a workbench">
        <rect x="276" y="400" width="276" height="236" fill="url(#gDesk)"/>
      </g>
      <g role="img" aria-label="Photo: gloved hand smoothing wet concrete with a trowel">
        <rect x="552" y="400" width="270" height="236" fill="url(#gTrowel)"/>
      </g>
      <path d="M276 0 H822 V486 C760 500 660 482 552 452 C470 420 360 405 276 428 Z" fill="var(--white)"/>

      <g role="img" aria-label="Photo: worker in a hard hat checking a tablet on site">
        <path d="M642 26 H798 V258 H682 Q642 258 642 218 Z" fill="url(#gTablet)"/>
      </g>
      <rect x="798" y="80" width="5" height="122" fill="var(--teal)"/>
    </svg>

    <div class="block body-copy justify" style="left:24px; top:30px; width:230px;">
      <h2 class="title">Our<br>Services</h2>
      <div class="title-rule"></div>
      <p style="font-size:10.6px; line-height:13.5px;">Alit moloratem ate derupta ssimus provit ut offic teces ius, sundigenis vid quis pres enimaximpel ipsuntore nihilles sequi sum velit autem. Nequi doluptatusam atem voloreprerio temostioreni unto consed ma aut a nonsequaepro ex ea vent aut quiatibus re modignihit, oditibus aspel il eium fugiat quaes nistotatur auditatius.</p>
      <p style="font-size:10.6px; line-height:13.5px;">Vit re necto quibusant dolut ipientiores millitas deniendam non re quidictur aut repere nobit, cori quaectur, quam ut volestem re lati deribus alique is saectet aut quae ommodit ommodi iliquant haris modit aliquo eum quae rempori bearibus asitat es dolectus.</p>
      <p style="font-size:10.6px; line-height:13.5px;">Metur, aut harum repro consedit aborum rent volorro venihic te voluptas molupturepd ex et et odit qui qui omnihil iquuntium que cus niaspedut optatem Metur, aut harum repro consedit aborum rent volorro venihic te voluptas molupturepd ex et et odit qui qui omnihil iquuntium que cus niaspedut optatem</p>
      <p style="font-size:10.6px; line-height:13.5px;">Metur, aut harum repro consedit aborum rent volorro venihic te voluptas</p>
    </div>

    <h2 class="envelope-title">BUILDING ENVELOPE:</h2>
    <div class="envelope-rule"></div>

    <div class="service-col" style="left:290px; top:68px; width:176px;">
      <div class="service"><h3>Concrete Repairs</h3><ul><li>Balcony slabs</li><li>Shear Walls</li><li>Beams &amp; Columns</li></ul></div>
      <div class="service"><h3>Masonry Repairs</h3><ul><li>Brick, Block &amp; Stone replacement</li><li>Tuck pointing</li><li>Through wall flashing</li><li>Coating (Sealer, Elastomeric, Silicone and Architectural coatings)</li></ul></div>
      <div class="service"><h3>Sealant Replacement</h3><ul><li>Window wall and glazing system sealants</li><li>Precast sealants</li><li>Masonry sealants</li><li>Balcony perimeter joints</li><li>Waterproofing</li><li>Balconies &amp; Terraces thin system</li><li>Garbage &amp; Mechanical rooms</li><li>Parking Garage Structures</li></ul></div>
    </div>

    <div class="service-col" style="left:466px; top:68px; width:172px;">
      <div class="service"><h3>Concrete Repairs</h3><ul><li>Partial slab replacement</li><li>Top/under side repairs</li><li>Hydro demolition</li><li>Columns, Beams and Shear Walls</li><li>Catch basins &amp; trench drains</li><li>Staircases</li></ul></div>
      <div class="service"><h3>Waterproofing</h3><ul><li>Vehicular thin system (drive aisles, parking bays, ramps, etc.)</li><li>Hot applied waterproofing (Ramps and Roof decks)</li><li>Expansion joints repairs/ replacement</li><li>Mastic waterproofing system</li><li>Foundation wall crack injections</li><li>Crystalline waterproofing</li></ul></div>
      <div class="service"><h3>Ramp Remediation</h3><ul><li>Electric heating cables</li><li>Asphalt, Interlocking, Mastic and Concrete</li></ul></div>
    </div>

    <div class="service-col" style="left:644px; top:268px; width:172px;">
      <div class="service"><h3>Miscellaneous</h3><ul><li>Railings remediation and replacement</li><li>Outside garbage pad enclosures</li><li>Retaining walls repair/ replacement</li><li>Weeping tile systems</li><li>Safety bollards &amp; precast curbs installation</li><li>Side walks, curbs, interlocking, asphalt and concrete pads</li><li>Balconies and Parking garages painting</li><li>Area drains replacements</li><li>Etc.</li></ul></div>
    </div>
  </section>

</div>
</body>
</html>
```